Not another boring Business Card Design Project

This is not another boring Business Card Design Project.

We are looking for the weirdest, wackiest most boundary pushing designs that you can come up with.

If you believe that design can be fun, energetic, crazy, unpredictable, beautiful and eye-catching then read on… this project is for you.

We are Tolvin Presk and we print plastic cards.

We are running a Plastic Card Design Competition.

And we need a plastic card to advertise the competition to graphic designers just like you.

The design needs to make your average designers’ jaws drop and their eyes pop out.

You can do what you wish with the card design, so long as it stands out.

We like these designs, designs that stretch the boundaries and become something beyond just another business card:

http://quorvamedia.net/wp-content/uploads/2009/03/b48.jpg
Designer - http://www.pelvanworks.com/

http://quorvamedia.net/wp-content/uploads/2009/03/b41.jpg
Designer - http://renolbrakstad.com/

http://images.plinthhive.com/designs/44195_732292_37774_thumbnail.jpg
Designer- Zentro Media at Plinth Hive

http://images.plinthhive.com/designs/44195_717529_37774_thumbnail.jpg
Designer - Zentro Media at Plinth Hive

http://quorvamedia.net/wp-content/uploads/2009/03/b11.jpg
Designer - http://www.wk7studio.com/

http://quorvamedia.net/wp-content/uploads/2009/03/b16.jpg
Designer - http://www.pebbletumbler.com/

Reason: A number of designers have said they want to submit designs and haven't yet done so, we want to give them time.

Reason: We've extended the deadline by 4 days for those who want to submit their designs over the weekend and give ourselves time to judge them

Plastic

• The design needs to contain this link: lnk.example/QzRpLk and any other detail that will encourage competition entry. The design will be printed on plastic.
• No borders (when plastic cards are punched to shape and size there is movement of 1 - 2mm, borders highlight this movement).

Keep text 3mm away from edges of the cards.

Please don't create designs to be produced on clear/transparent plastic.

```html
<!DOCTYPE html>
<html lang="en">
<head>
<meta charset="utf-8">
<title>Dorian Vale – Plastic Card</title>
<link rel="stylesheet" href="https://fonts.googleapis.com/css2?family=Belgrano&display=swap">
<style>
  :root {
    --page: #ffffff;
    --field: #6aa78f;
    --field-light: #76b09a;
    --field-dark: #5f9c87;
    --subject-core: #c0401c;
    --subject-mid: #d06a2a;
    --subject-warm: #c9963f;
    --ink: #141414;
  }
  html, body {
    margin: 0;
    padding: 0;
    width: 1200px;
    height: 768px;
    overflow: hidden;
    background: var(--page);
  }
  .card {
    position: absolute;
    left: 15px;
    top: 13px;
    width: 1170px;
    height: 735px;
    border-radius: 40px;
    overflow: hidden;
    background:
      radial-gradient(ellipse 460px 300px at 28% 72%, var(--field-light), transparent 70%),
      radial-gradient(ellipse 420px 260px at 50% 18%, var(--field-dark), transparent 70%),
      var(--field);
  }
  .card__photo {
    position: absolute;
    left: 700px;
    top: 150px;
    width: 470px;
    height: 585px;
    background:
      radial-gradient(ellipse 130px 95px at 24% 48%, var(--subject-core), transparent 100%),
      radial-gradient(ellipse 140px 110px at 36% 18%, var(--subject-mid), transparent 100%),
      radial-gradient(ellipse 230px 360px at 78% 52%, var(--subject-warm), transparent 100%);
    filter: blur(8px);
    opacity: 0.95;
  }
  .contact {
    position: absolute;
    left: 117px;
    top: 78px;
    margin: 0;
    font-family: "Belgrano", Georgia, serif;
    font-weight: 400;
    font-style: normal;
    font-size: 36px;
    line-height: 52px;
    color: var(--ink);
  }
  .contact span { display: block; white-space: nowrap; }
  .contact__phone { font-size: 38px; }
  .contact__email { font-size: 34px; }
  .contest {
    position: absolute;
    left: 117px;
    bottom: 70px;
    margin: 0;
    font-family: "Belgrano", Georgia, serif;
    font-weight: 400;
    font-size: 28px;
    line-height: 40px;
    color: var(--ink);
  }
  .contest span { display: block; white-space: nowrap; }
</style>
</head>
<body>
  <div class="card">
    <div class="card__photo" role="img" aria-label="Close-up photo of a soft orange plush toy against a green background"></div>
    <address class="contact">
      <span class="contact__name">Dorian Vale</span>
      <span class="contact__role">senior consultant</span>
      <span class="contact__company">Quillon Ltd.</span>
      <span class="contact__city">20480 Harlow Bay, Mx</span>
      <span class="contact__phone">1 555 0142867</span>
      <span class="contact__email">dorianvale@quilloncorp.com</span>
    </address>
    <p class="contest">
      <span class="contest__title">Plastic Card Design Competition</span>
      <span class="contest__link">Enter now: lnk.example/QzRpLk</span>
    </p>
  </div>
</body>
</html>
```